Executive Business Card for Healthcare Company [Need Today]

I need a business card design for a healthcare company. The only branding the company has thus far is a logo. The cards will be utilized by company executives. The design I envision will be vibrant and appealing but with a corporate feel. They shouldn't be too casual or playful. I would like to complete this project TODAY if possible.

Target Market(s)

Healthcare vendors, other executives in healthcare and pharmaceuticals

Industry/Entity Type

Pharmaceutical

Contact Information for Business Card

See attachment

Font styles to use
Serif
Sans Serif

Colors

Designer to choose colors to be used in the design.

```html
<!DOCTYPE html>
<html lang="en">
<head>
<meta charset="utf-8">
<title>Corvane Therapeutics – Business Card</title>
<link rel="stylesheet" href="https://fonts.googleapis.com/css2?family=Arimo:wght@400;700&display=swap">
<style>
  :root {
    --backdrop: #3a3a3a;
    --card-front: #ececec;
    --card-back: #ffffff;
    --teal: #2fbdc4;
    --green: #5cbf94;
    --ink: #1f1f1f;
    --rule: #8a8a8a;
    --pattern-a: #e4f5f1;
    --pattern-b: #f6fcfb;
  }
  * { box-sizing: border-box; margin: 0; padding: 0; }
  html, body { width: 1200px; height: 900px; overflow: hidden; }
  body {
    background: var(--backdrop);
    font-family: "Arimo", Arial, sans-serif;
    color: var(--ink);
    position: relative;
  }
  .card {
    position: absolute;
    top: 170px;
    width: 347px;
    height: 561px;
    overflow: hidden;
  }
  .card--front { left: 259px; background: var(--card-front); }
  .card--back { left: 631px; background: var(--card-back); }

  .brand {
    position: absolute;
    top: 110px;
    left: 32px;
    display: flex;
    align-items: center;
    gap: 14px;
  }
  .brand__circle {
    width: 86px; height: 86px;
    border: 4px solid var(--green);
    border-radius: 50%;
    flex: none;
  }
  .brand__name {
    font-size: 25px;
    font-weight: 400;
    color: var(--teal);
    line-height: 1.15;
  }

  .contact {
    position: absolute;
    top: 310px;
    left: 0; right: 0;
    text-align: center;
  }
  .contact__name {
    font-size: 19px;
    font-weight: 700;
    letter-spacing: 0.3px;
  }
  .contact__name .first { color: var(--teal); }
  .contact__name .last { color: var(--green); }
  .contact__title { font-size: 15.5px; margin-top: 3px; }

  .icon-rule {
    display: flex;
    align-items: center;
    justify-content: center;
    gap: 3px;
    margin: 9px auto 6px;
    width: 206px;
  }
  .icon-rule__line { flex: 1; height: 1px; background: var(--rule); }
  .icon-rule svg { width: 14px; height: 14px; flex: none; }

  .contact__line { font-size: 15.5px; line-height: 20.5px; }
  .divider { width: 150px; height: 1px; background: var(--rule); margin: 10px auto 12px; }
  .company { font-size: 16px; font-weight: 700; color: var(--green); letter-spacing: 0.3px; }

  .back-pattern {
    position: absolute; inset: 0;
    background: linear-gradient(160deg, var(--pattern-b), var(--pattern-a) 50%, var(--pattern-b));
  }
  .back-name {
    position: absolute;
    top: 262px;
    left: 0; right: 0;
    text-align: center;
    font-size: 62px;
    font-weight: 400;
    color: var(--teal);
    letter-spacing: 1px;
  }
</style>
</head>
<body>
  <section class="card card--front" aria-label="Business card front">
    <div class="brand">
      <span class="brand__circle"></span>
      <span class="brand__name">Corvane<br>Therapeutics</span>
    </div>

    <div class="contact">
      <p class="contact__name"><span class="first">MARTIN</span> <span class="last">HALE</span></p>
      <p class="contact__title">Senior Director of Marketing</p>

      <div class="icon-rule">
        <span class="icon-rule__line"></span>
        <svg viewBox="0 0 14 14" aria-label="Phone"><circle cx="7" cy="7" r="6.3" fill="none" stroke="#2fbdc4" stroke-width="1"/><path d="M4.3 5.2c0-.6.5-1 1-1h3.4c.5 0 1 .4 1 1v.6H4.3zM4.8 6.4h4.4l.6 3.4H4.2z" fill="#2fbdc4"/></svg>
        <svg viewBox="0 0 14 14" aria-label="Mobile"><circle cx="7" cy="7" r="6.3" fill="none" stroke="#2fbdc4" stroke-width="1"/><rect x="5" y="3.5" width="4" height="7" rx=".7" fill="none" stroke="#2fbdc4" stroke-width="1"/></svg>
        <svg viewBox="0 0 14 14" aria-label="Email"><circle cx="7" cy="7" r="6.3" fill="none" stroke="#2fbdc4" stroke-width="1"/><rect x="4" y="4.8" width="6" height="4.4" fill="none" stroke="#2fbdc4" stroke-width=".9"/><path d="M4 4.8l3 2.4 3-2.4" fill="none" stroke="#2fbdc4" stroke-width=".9"/></svg>
        <span class="icon-rule__line"></span>
      </div>

      <p class="contact__line">555-210-4836</p>
      <p class="contact__line">555-318-7092</p>
      <p class="contact__line">mhale@corvanerx.com</p>

      <div class="divider"></div>

      <p class="company">CORVANE THERAPEUTICS, LLC</p>
      <p class="contact__line">418 W Harmon Avenue</p>
      <p class="contact__line">Easton, PA 18042</p>
    </div>
  </section>

  <section class="card card--back" aria-label="Business card back">
    <div class="back-pattern" role="img" aria-label="Repeating pattern of the company mark in pale mint circles"></div>
    <p class="back-name">Corvane</p>
  </section>
</body>
</html>
```